I need a business card for myself, being a proprietor of a funeral parlor based in Manila. I'd like the card to have either of the following:
White Font on Black Background
or
Black Font on White Background
No logo is needed however I will appreciate any efforts to show a symbol of eternal happiness, aptly designed with above mentioned colors in mind.
Company name, address and contact on the lower right corner.
Logo or symbol anywhere.
Brightvale Funeral Services
+639174412870
dariel4412@quillmail.com
corner of Corvina Avenue and Halberd Street
Makati City, Philippines
Thank you.
Update: Please include a small dove in your design. You are free to choose where you would like it on the card.

```html
<!DOCTYPE html>
<html lang="en">
<head>
<meta charset="utf-8">
<title>Brightvale Funeral Services – Business Card</title>
<link href="https://fonts.googleapis.com/css2?family=Open+Sans:wght@400;600&display=swap" rel="stylesheet">
<style>
  :root {
    --page-bg: #1c1c1c;
    --card-bg: #050505;
    --ink: #ffffff;
    --ink-soft: #d9d9d9;
    --rule: #9a9a9a;
    --tag-ink: #050505;
  }
  * { box-sizing: border-box; margin: 0; padding: 0; }
  html, body {
    width: 1200px;
    height: 871px;
    overflow: hidden;
    background: var(--page-bg);
    font-family: "Open Sans", Arial, sans-serif;
  }
  .canvas {
    position: relative;
    width: 1200px;
    height: 871px;
    display: flex;
    align-items: center;
    justify-content: center;
  }
  .business-card {
    position: relative;
    width: 900px;
    height: 514px;
    background: var(--card-bg);
    display: flex;
    align-items: center;
    padding: 0 60px 0 80px;
    box-shadow: 0 20px 50px rgba(0,0,0,0.6);
  }
  .brand {
    display: flex;
    align-items: center;
    gap: 16px;
    width: 380px;
  }
  .brand-mark {
    flex: none;
    width: 22px;
    height: 22px;
    border-radius: 50%;
    background: var(--ink);
  }
  .brand-name {
    color: var(--ink);
    font-weight: 600;
    font-size: 27px;
    line-height: 1.2;
  }
  .divider {
    width: 1px;
    height: 190px;
    background: var(--rule);
    margin: 0 30px 0 20px;
  }
  .contact-list {
    list-style: none;
    color: var(--ink-soft);
    font-size: 17px;
    line-height: 1.35;
  }
  .contact-item {
    display: flex;
    align-items: flex-start;
    gap: 12px;
    margin-bottom: 4px;
  }
  .contact-tag {
    flex: none;
    width: 18px;
    height: 18px;
    margin-top: 2px;
    background: var(--ink);
    color: var(--tag-ink);
    font-size: 12px;
    font-weight: 600;
    display: flex;
    align-items: center;
    justify-content: center;
  }
</style>
</head>
<body>
  <main class="canvas">
    <section class="business-card">
      <div class="brand">
        <span class="brand-mark" aria-hidden="true"></span>
        <span class="brand-name">Brightvale Funeral Services</span>
      </div>
      <div class="divider" aria-hidden="true"></div>
      <ul class="contact-list">
        <li class="contact-item"><span class="contact-tag">P</span><span>+63-9174412870</span></li>
        <li class="contact-item"><span class="contact-tag">E</span><span>dariel4412@quillmail.com</span></li>
        <li class="contact-item"><span class="contact-tag">A</span><span>corner of Corvina Avenue and Halberd Street<br>Makati City, Philippines</span></li>
      </ul>
    </section>
  </main>
</body>
</html>
```